KLV Home Loans Website

Need a web site designed for a Professional Mortgage company along the lines of the draft site www.klvhomeloans.com.au

The main purpose of the site is to provide a professional image of the company and capture email address's and send out simple messages. ie "INTEREST RATE SPECIAL 4.5% FOR THE MONTH OF JUNE" or whatever...basically short punchy messages to hook people.

The content is important but a lot of that can be provided by links to our lender panel, several of which have been set up.

Most people will want to know current interest rates, and how much they can borrow along with what it will cost. There are various calculators embedded in the lenders sites such as "Repayment Calculators" Borrow Capacity Calculators" Stamp Duty Calculators"

These would be nice to have on site, but if to costly or difficult to start the links can suffice.

The site will need to be updated/amended regularily.

Example "Interest Rate Special" or "Current Special Offer" sections would be required and would need to be easyily editable and in fact would need to be able to switch them off if there is no special running.

Target Market(s)

Target market is a broad spectrum of people from young couple buying first home to older couples investing.

Industry/Entity Type

It Company

Requirements
Must have
• email capture, preferably need to enter email to enter site.

```html
<!DOCTYPE html>
<html lang="en">
<head>
<meta charset="utf-8">
<title>KLV Home Loans Services</title>
<link href="https://fonts.googleapis.com/css2?family=Open+Sans:wght@300;400;600;700&display=swap" rel="stylesheet">
<style>
  :root {
    --black: #000;
    --header-top: #262626;
    --header-bottom: #000;
    --white: #fff;
    --text-muted: #bdbdbd;
    --text-dim: #8c8c8c;
    --orange: #f6a612;
    --promo: #fdb516;
    --promo-border: #ffe7a6;
    --card-top: #2d2d2d;
    --card-bottom: #0d0d0d;
    --card-border: #5a5a5a;
    --footer: #1c1c1c;
    --divider: #4a4a4a;
    --social: #3b6db3;
  }
  * { margin: 0; padding: 0; box-sizing: border-box; }
  html, body { width: 1080px; height: 1200px; overflow: hidden; background: var(--black); }
  body { font-family: "Open Sans", Arial, sans-serif; color: var(--white); position: relative; }

  .site-header { position: absolute; left: 0; top: 0; width: 1080px; height: 121px;
    background: linear-gradient(var(--header-top), var(--header-bottom)); border-bottom: 1px solid #333; }
  .brand { position: absolute; left: 68px; top: 22px; width: 260px; text-align: center;
    font-size: 29px; font-weight: 400; line-height: 40px; color: var(--white); }
  .phone { position: absolute; right: 76px; top: 16px; display: flex; align-items: center; gap: 8px;
    color: var(--orange); font-size: 23px; }
  .main-nav { position: absolute; right: 58px; top: 66px; display: flex; }
  .main-nav a { color: var(--white); text-decoration: none; font-size: 16px; padding: 0 18px;
    line-height: 22px; border-left: 1px solid var(--divider); }
  .main-nav a:first-child { border-left: none; }
  .main-nav a:last-child { padding-right: 0; }

  .hero { position: absolute; left: 0; top: 122px; width: 1080px; height: 433px;
    background: linear-gradient(100deg, #e9e4df 0%, #d7c3b0 25%, #cfd8df 50%, #e8d8cc 75%, #f1ede8 100%); }
  .promo { position: absolute; left: 747px; top: 197px; width: 280px; height: 171px;
    background: var(--promo); border: 2px solid var(--promo-border); padding: 16px 20px; }
  .promo-title { font-size: 24px; line-height: 26px; font-weight: 400; }
  .promo-sub { font-size: 18px; line-height: 22px; display: block; }
  .promo p { font-size: 12px; line-height: 18px; margin-top: 8px; color: #fff7e0; }
  .promo-btn { display: inline-block; margin-top: 8px; background: #000; color: var(--white);
    font-size: 13px; font-weight: 700; padding: 7px 19px; border-radius: 3px; }
  .slider-dots { position: absolute; left: 509px; top: 409px; display: flex; gap: 4px; }
  .slider-dots span { width: 13px; height: 13px; border-radius: 50%; background: #1a1a1a; }

  .welcome { position: absolute; left: 58px; top: 590px; width: 665px; }
  .welcome h1 { font-size: 26px; font-weight: 400; line-height: 36px; margin-bottom: 8px; }
  .welcome p { font-size: 12.5px; line-height: 21.3px; color: var(--text-muted); margin-bottom: 9px; }

  .features { position: absolute; left: 59px; top: 832px; display: flex; gap: 14px; }
  .feature { width: 210px; }
  .feature-photo { height: 108px; }
  .feature h2 { font-size: 16px; font-weight: 400; color: var(--orange); margin: 12px 0 5px 3px; }
  .feature p { font-size: 12.5px; line-height: 17.5px; color: var(--text-muted); padding-left: 3px; }

  .tool-card { position: absolute; left: 753px; width: 278px; height: 101px;
    background: linear-gradient(var(--card-top), var(--card-bottom)); border: 1px solid var(--card-border);
    border-radius: 3px; padding: 14px 22px; }
  .tool-card h3 { font-size: 19px; font-weight: 400; line-height: 26px; color: var(--orange); }
  .tool-card h3 span { display: block; color: var(--white); font-size: 20px; }
  .tool-card p { font-size: 12.5px; color: var(--text-muted); margin-top: 2px; }
  .tool-card svg { position: absolute; right: 18px; top: 14px; }

  .latest { position: absolute; left: 755px; top: 815px; width: 278px; height: 220px;
    background: linear-gradient(120deg, #f2f2f2, #d9cfc6 50%, #ece8e4); }
  .latest-caption { position: absolute; left: 0; bottom: 0; width: 100%; height: 63px;
    background: rgba(40,40,40,0.85); padding: 7px 17px; }
  .latest-caption h3 { font-size: 21px; font-weight: 400; line-height: 28px; }
  .latest-caption p { font-size: 12.5px; color: var(--text-muted); }

  .site-footer { position: absolute; left: 0; top: 1098px; width: 1080px; height: 102px; background: var(--footer); }
  .footer-nav { position: absolute; left: 65px; top: 27px; font-size: 14px; color: var(--text-muted); }
  .footer-nav a { color: #d8d8d8; text-decoration: none; }
  .footer-nav .sep { margin: 0 6px; }
  .copyright { position: absolute; left: 65px; top: 58px; font-size: 12.5px; color: var(--text-dim); }
  .social { position: absolute; left: 935px; top: 24px; display: flex; gap: 10px; }
  .social span { width: 21px; height: 21px; background: var(--social); border-radius: 2px; }
</style>
</head>
<body>
  <header class="site-header">
    <div class="brand">KLV Home Loans<br>Services</div>
    <div class="phone">
      <svg width="26" height="26" viewBox="0 0 24 24" aria-hidden="true">
        <path d="M6.6 10.8a15 15 0 0 0 6.6 6.6l2.2-2.2c.3-.3.7-.4 1-.2 1.1.4 2.3.6 3.6.6.6 0 1 .4 1 1V20c0 .6-.4 1-1 1A17 17 0 0 1 3 4c0-.6.4-1 1-1h3.5c.6 0 1 .4 1 1 0 1.3.2 2.5.6 3.6.1.3 0 .7-.2 1z" fill="#fff"/>
      </svg>
      <span>555.010.2748</span>
    </div>
    <nav class="main-nav">
      <a href="#">Home</a><a href="#">About Us</a><a href="#">Our Clients</a><a href="#">Services</a><a href="#">Partners</a><a href="#">Join Us</a>
    </nav>
  </header>

  <section class="hero" role="img" aria-label="Photo of a smiling adviser with a clipboard meeting a young family and their dog on a sofa">
    <div class="promo">
      <div class="promo-title">GET REGISTER YOUR<span class="promo-sub">EMAIL ADDRESS NOW</span></div>
      <p>Aliquam nec erat at purus cursus inter-<br>dum Vestibulum ligula augue</p>
      <span class="promo-btn">CLICK HERE</span>
    </div>
    <div class="slider-dots"><span></span><span></span><span></span><span></span></div>
  </section>

  <section class="welcome">
    <h1>Welcome to KLV Home Loans Services Mainpage</h1>
    <p>Phasellus felis dolor, scelerisque a, tempus eget, lobortis id, libero. Donec scelerisque leo ac risus. Praesent sit amet est. In dictum, dolor eu dictum porttitor, enim felis viverra mi, eget luctus massa purus quis odio. Etiam nulla massa, pharetra facilisis, volutpat in, imperdiet sit amet, sem. Aliquam nec erat at purus cursus interdum. Vestibulum ligula augue, bibendum accumsan, vestibulum ut, commodo a, mi. Morbi ornare gravida elit. Integer congue, augue et malesuada iaculis, ipsum dui aliquet felis, at cursus magna nisl nec elit.</p>
    <p>Phasellus felis dolor, scelerisque a, tempus eget, lobortis id, libero. Donec scelerisque leo ac risus. Praesent sit amet est. In dictum, dolor eu dictum porttitor, enim felis viverra mi</p>
  </section>

  <section class="features">
    <article class="feature">
      <div class="feature-photo" role="img" aria-label="Photo of a happy couple holding up new house keys" style="background:linear-gradient(135deg,#6b7a3a,#c9a07c 55%,#8a6a4e)"></div>
      <h2>FEATURED SERVICE</h2>
      <p>Donec scelerisque leo ac risus Praesent sit amet est In dictu dolor eu dictum porttitor</p>
    </article>
    <article class="feature">
      <div class="feature-photo" role="img" aria-label="Photo of cupped hands holding a small model house" style="background:linear-gradient(135deg,#f4f4f4,#d8c4b4 50%,#eeeeee)"></div>
      <h2>FEATURED SERVICE</h2>
      <p>Donec scelerisque leo ac risus Praesent sit amet est In dictu dolor eu dictum porttitor</p>
    </article>
    <article class="feature">
      <div class="feature-photo" role="img" aria-label="Photo of an older couple reviewing papers with an adviser" style="background:linear-gradient(135deg,#d8d2c8,#a88e76 50%,#3a3430)"></div>
      <h2>FEATURED SERVICE</h2>
      <p>Donec scelerisque leo ac risus Praesent sit amet est In dictu dolor eu dictum porttitor</p>
    </article>
  </section>

  <a class="tool-card" style="top:589px" href="#">
    <h3>INTEREST<span>CALCULATOR</span></h3>
    <p>Nunc porta convallis pede.</p>
    <svg width="70" height="70" viewBox="0 0 70 70" aria-hidden="true">
      <rect x="3" y="3" width="64" height="64" rx="8" fill="none" stroke="#fff" stroke-width="4"/>
      <rect x="13" y="12" width="44" height="12" fill="#fff"/>
      <g fill="#fff">
        <rect x="13" y="30" width="9" height="7"/><rect x="25" y="30" width="9" height="7"/><rect x="37" y="30" width="9" height="7"/><rect x="49" y="30" width="8" height="7"/>
        <rect x="13" y="40" width="9" height="7"/><rect x="25" y="40" width="9" height="7"/><rect x="37" y="40" width="9" height="7"/><rect x="49" y="40" width="8" height="17"/>
        <rect x="13" y="50" width="9" height="7"/><rect x="25" y="50" width="9" height="7"/><rect x="37" y="50" width="9" height="7"/>
      </g>
    </svg>
  </a>

  <a class="tool-card" style="top:701px" href="#">
    <h3>REPAYMENT<span>CALCULATOR</span></h3>
    <p>Nunc porta convallis pede.</p>
    <svg width="84" height="70" viewBox="0 0 84 70" aria-hidden="true">
      <g transform="rotate(-20 30 30)">
        <rect x="6" y="12" width="52" height="32" rx="3" fill="#111" stroke="#fff" stroke-width="4"/>
        <circle cx="32" cy="28" r="10" fill="#fff"/>
        <text x="32" y="33" text-anchor="middle" font-family="Open Sans, sans-serif" font-size="14" font-weight="700" fill="#111">$</text>
      </g>
      <rect x="26" y="32" width="54" height="32" rx="3" fill="#111" stroke="#fff" stroke-width="4"/>
      <circle cx="53" cy="48" r="10" fill="#fff"/>
      <text x="53" y="53" text-anchor="middle" font-family="Open Sans, sans-serif" font-size="14" font-weight="700" fill="#111">$</text>
    </svg>
  </a>

  <section class="latest" role="img" aria-label="Photo of a smiling couple relaxing together at home">
    <div class="latest-caption">
      <h3>LATEST MORTGAGE</h3>
      <p>Nunc porta convallis pede.</p>
    </div>
  </section>

  <footer class="site-footer">
    <nav class="footer-nav">
      <a href="#">Home</a><span class="sep">/</span><a href="#">About Us</a><span class="sep">/</span><a href="#">Our Clients</a><span class="sep">/</span><a href="#">Services</a><span class="sep">/</span><a href="#">Partners</a><span class="sep">/</span><a href="#">Join Us</a>
    </nav>
    <p class="copyright">© 2013 Company Name.&nbsp; All right reserved</p>
    <div class="social" aria-label="Social links"><span></span><span></span><span></span></div>
  </footer>
</body>
</html>
```